Modern Venture Capital website

Design a modern website for a venture capital firm. This website should be modern and beautiful and be on par with other Venture Capital websites. I have a logo and a hero video I'd like to use. Link to hero video: https://files.vantoria.example/f/9Xk2Lm7qPz4Rt8Wb3Nc6Hd5Jy1Gs0Ve/view?ref=share_link

Preference will be given to the best design that combines design with the best images and digital content. That means no generic free stock videos 😅

I currently built a wix website to give you an idea of what content needs to be on the website. Depending on your design it can be 3 pages, or one long page. I will leave it up to you.

WEBSITE: https://brelmor58204.pagecraftly.example/my-site-4

Target Market(s)

Mid-career professionals, individuals interested in Venture Capital

Industry/Entity Type

Finance, venture capital, startups

Requirements
Must have
• must use the hero video I have and must use my logo. Must use high quality images that matches the website design - no generic stock images

```html
<!DOCTYPE html>
<html lang="en">
<head>
<meta charset="utf-8">
<title>Nocturne Ventures</title>
<link rel="stylesheet" href="https://fonts.googleapis.com/css2?family=Inter:wght@400;500;600;700&family=Poppins:wght@700&display=swap">
<style>
  :root {
    --accent: #cfee00;
    --ink: #0b0b0b;
    --night: #0c0a08;
    --card: #2c2e31;
    --white: #ffffff;
    --muted: #9a9a9a;
    --body: #1c1c1c;
    --grey-text: #6b6b6b;
    --chip: #3a3b3d;
  }
  * { box-sizing: border-box; margin: 0; padding: 0; }
  html, body { width: 1200px; height: 1200px; overflow: hidden; background: var(--white); }
  body { position: relative; font-family: "Inter", sans-serif; color: var(--body); }

  .hero { position: absolute; left: 0; top: 0; width: 1200px; height: 550px; overflow: hidden; background: var(--night); }
  .hero-backdrop { position: absolute; inset: 0;
    background:
      radial-gradient(circle at 660px 110px, rgba(120,100,70,0.45) 0, rgba(60,50,35,0.25) 70px, transparent 120px),
      radial-gradient(ellipse at 600px 250px, rgba(70,55,35,0.35), transparent 70%),
      linear-gradient(180deg, #17130f 0%, #0e0b08 60%, #050505 100%); }

  .nav { position: absolute; left: 0; top: 0; width: 1200px; height: 43px; background: rgba(0,0,0,0.35); }
  .brand { position: absolute; left: 193px; top: 7px; color: var(--white); }
  .brand-name { font-family: "Poppins", sans-serif; font-weight: 700; font-size: 20px; line-height: 20px; display: block; }
  .brand-sub { font-family: "Poppins", sans-serif; font-weight: 700; font-size: 6.5px; letter-spacing: 2.6px; display: block; margin-top: 1px; }
  .nav-link { position: absolute; top: 16px; font-size: 10px; color: var(--white); }
  .nav-cta { position: absolute; left: 920px; top: 7px; width: 102px; height: 28px; background: var(--accent); color: var(--ink); font-size: 10px; border-radius: 2px; display: flex; align-items: center; justify-content: center; }

  .hero-title { position: absolute; left: 0; top: 100px; width: 1200px; text-align: center; font-size: 40px; font-weight: 500; line-height: 48px; color: var(--white); }
  .hero-title .accent { color: var(--accent); }
  .hero-lede { position: absolute; left: 370px; top: 206px; width: 460px; text-align: center; font-size: 11px; line-height: 16px; color: var(--muted); }
  .btn { position: absolute; top: 253px; height: 29px; font-size: 10px; border-radius: 2px; display: flex; align-items: center; justify-content: center; }
  .btn-primary { left: 525px; width: 72px; background: var(--accent); color: var(--ink); }
  .btn-secondary { left: 607px; width: 72px; background: var(--chip); color: #e6e6e6; }

  .portfolio-card { position: absolute; top: 315px; height: 204px; overflow: hidden; }
  .portfolio-card .photo { position: absolute; inset: 0; }
  .portfolio-label { position: absolute; left: 22px; bottom: 14px; color: var(--white); font-weight: 700; font-size: 17px; letter-spacing: 1px; }
  .card-a { left: 168px; width: 190px; }
  .card-a .photo { background: linear-gradient(90deg, #0c0a08 0%, #4a3b2e 40%, #6a5240 100%); }
  .card-b { left: 367px; width: 304px; }
  .card-b .photo { background: linear-gradient(180deg, #5e4a3c 0%, #3d4650 55%, #0e0c0a 100%); }
  .card-c { left: 681px; width: 305px; }
  .card-c .photo { background: linear-gradient(180deg, #3a4042 0%, #4c5550 50%, #120e0c 100%); }
  .card-d { left: 995px; width: 59px; }
  .card-d .photo { background: linear-gradient(90deg, #6b5a4e, #1a1512); }
  .hero-rule { position: absolute; left: 20px; top: 550px; width: 1160px; height: 1px; background: var(--ink); }

  .tag { position: absolute; font-size: 10px; color: var(--body); display: flex; align-items: center; }
  .tag::before { content: ""; width: 9px; height: 9px; background: var(--accent); margin-right: 7px; }
  .tag-founders { left: 195px; top: 603px; }
  .founders-copy { position: absolute; left: 195px; top: 632px; width: 370px; font-size: 10.6px; line-height: 20.5px; color: var(--body); }

  .stats { position: absolute; left: 195px; top: 789px; width: 390px; height: 75px; background: var(--ink); border-radius: 2px; }
  .stat { position: absolute; top: 12px; width: 90px; text-align: center; }
  .stat-value { display: block; font-size: 31px; font-weight: 600; line-height: 36px; color: var(--accent); }
  .stat-label { display: block; font-size: 8px; color: var(--white); margin-top: 3px; }
  .founders-photo { position: absolute; left: 615px; top: 600px; width: 390px; height: 264px; border-radius: 2px;
    background: linear-gradient(90deg, #c48a5a 0%, #3d7d96 30%, #2aa9d0 55%, #13335a 80%, #0d1e3b 100%); }

  .tag-vc { left: 182px; top: 953px; }
  .vc-copy { position: absolute; left: 179px; top: 980px; width: 830px; font-size: 11px; line-height: 16px; color: var(--grey-text); }
  .benefit { position: absolute; top: 1040px; width: 214px; height: 200px; background: var(--card); border-radius: 25px 25px 0 0; }
  .benefit svg { position: absolute; left: 22px; top: 31px; width: 52px; height: 46px; }
  .benefit-title { position: absolute; left: 22px; top: 104px; width: 180px; font-size: 14px; font-weight: 700; line-height: 16px; color: var(--white); }
</style>
</head>
<body>
  <header class="hero">
    <div class="hero-backdrop" role="img" aria-label="Night sky with a rising moon over clouds"></div>
    <nav class="nav">
      <div class="brand"><span class="brand-name">Nocturne</span><span class="brand-sub">VENTURES</span></div>
      <span class="nav-link" style="left:661px">Home</span>
      <span class="nav-link" style="left:710px">Join VC</span>
      <span class="nav-link" style="left:762px">Startups</span>
      <span class="nav-link" style="left:815px">Insights</span>
      <span class="nav-link" style="left:867px">Investors</span>
      <span class="nav-cta">Apply for Funding</span>
    </nav>
    <h1 class="hero-title">Venture Capital for the<br><span class="accent">Late-Night</span> Hustlers</h1>
    <p class="hero-lede">At Nocturne Ventures, we provide strategic capital and unparalleled support to startups that are shaping the future of decentralized technology.</p>
    <span class="btn btn-primary">Get started</span>
    <span class="btn btn-secondary">Contact Us</span>

    <div class="portfolio-card card-a"><div class="photo" role="img" aria-label="Founder seated in a busy café"></div></div>
    <div class="portfolio-card card-b"><div class="photo" role="img" aria-label="Smiling founder with arms crossed in an office"></div><span class="portfolio-label">VELTRA</span></div>
    <div class="portfolio-card card-c"><div class="photo" role="img" aria-label="Founder presenting beside a laptop"></div><span class="portfolio-label" style="left:34px;font-size:16px">Quillfern</span></div>
    <div class="portfolio-card card-d"><div class="photo" role="img" aria-label="Founder portrait, partly in view"></div><span class="portfolio-label" style="left:18px;font-size:16px">Harbo</span></div>
  </header>
  <div class="hero-rule"></div>

  <section>
    <span class="tag tag-founders">Simplifying success for founders</span>
    <p class="founders-copy">Our strength lies in our network. Our LPs and operating partners are all&nbsp; mid-to-senior level executives in their industries. They bring&nbsp; real-world corporate experience, offering strategic insights and operational support to help our portfolio companies scale efficiently. We cut&nbsp; through the noise and get to the core of your business fast. If we love&nbsp; what you’re building, we’ll move. If not, we’ll tell you quickly and&nbsp; respectfully. That lets you make</p>
    <div class="stats">
      <div class="stat" style="left:4px"><span class="stat-value">14</span><span class="stat-label">Pre-Seed / Seed</span></div>
      <div class="stat" style="left:101px"><span class="stat-value">50K</span><span class="stat-label">Check Size</span></div>
      <div class="stat" style="left:198px"><span class="stat-value">20%</span><span class="stat-label">Carried Interest</span></div>
      <div class="stat" style="left:290px;width:100px"><span class="stat-value">2.5%</span><span class="stat-label">Management Fee</span></div>
    </div>
    <div class="founders-photo" role="img" aria-label="Executive in a suit holding a tablet with glowing market charts above a city at dusk"></div>
  </section>

  <section>
    <span class="tag tag-vc">Become VC</span>
    <p class="vc-copy">At Nocturne Ventures, we’re opening the doors to a new kind of investor, mid-career professionals&nbsp; and aspiring VCs who want real skin in the game, not just exposure from&nbsp; the sidelines.</p>

    <div class="benefit" style="left:161px">
      <svg viewBox="0 0 52 46"><g fill="none" stroke="var(--accent)" stroke-width="4"><path d="M2 2 V40 H52"/></g><g fill="var(--accent)"><rect x="10" y="22" width="5" height="14"/><rect x="20" y="14" width="5" height="22"/><rect x="30" y="20" width="5" height="16"/><rect x="40" y="10" width="5" height="26"/></g></svg>
      <span class="benefit-title" style="top:114px">Hands on VC Work</span>
    </div>
    <div class="benefit" style="left:387px">
      <svg viewBox="0 0 52 46"><g fill="var(--accent)"><ellipse cx="28" cy="26" rx="19" ry="14"/><circle cx="28" cy="6" r="5"/><rect x="15" y="34" width="7" height="10" rx="2"/><rect x="32" y="34" width="7" height="10" rx="2"/><rect x="44" y="22" width="8" height="8" rx="2"/></g><path d="M9 24 q-7 0 -7 -6" fill="none" stroke="var(--accent)" stroke-width="3"/></svg>
      <span class="benefit-title">Earn Carry and Put Your Name on an Investment</span>
    </div>
    <div class="benefit" style="left:613px">
      <svg viewBox="0 0 52 46"><g fill="var(--accent)"><path d="M17 0 h18 a3 3 0 0 1 3 3 v7 h-5 v-5 h-14 v5 h-5 v-7 a3 3 0 0 1 3 -3z"/><rect x="0" y="11" width="52" height="15" rx="3"/><rect x="0" y="29" width="52" height="17" rx="3"/><rect x="21" y="23" width="10" height="9" rx="1"/></g></svg>
      <span class="benefit-title">Meaningful Opportunities to develop your career in Venture Capital</span>
    </div>
    <div class="benefit" style="left:839px">
      <svg viewBox="0 0 52 46"><g fill="var(--accent)"><circle cx="26" cy="12" r="9"/><circle cx="9" cy="15" r="6"/><circle cx="43" cy="15" r="6"/><path d="M12 40 a14 12 0 0 1 28 0 v3 h-28z"/><path d="M0 36 a9 8 0 0 1 14 -8 a16 14 0 0 0 -3 12 h-11z"/><path d="M52 36 a9 8 0 0 0 -14 -8 a16 14 0 0 1 3 12 h11z"/></g></svg>
      <span class="benefit-title">Join a community of Hustlers</span>
    </div>
  </section>
</body>
</html>
```